Stationary - Based On Previous Design

Basic stationary with a header and footer

Target Market(s)

Friends, Colleagues, More friendly than professional

Industry/Entity Type

legal/personal

Colors
00AB8E
00BBA5
67D7C9
C6EFE9
E9F9F6

Requirements
Must have
• Green & White
Nice to have
• I like the "G" on the business card and was thinking that would be for both G's in "PellowNote"
Should not have
• other colors

```html
<!DOCTYPE html>
<html lang="en">
<head>
<meta charset="utf-8">
<title>PellowNote Stationery</title>
<link rel="stylesheet" href="https://fonts.googleapis.com/css2?family=Domine:wght@700&family=Urbanist:wght@400;500&display=swap">
<style>
  :root {
    --green-deep: #00AB8E;
    --green: #00BBA5;
    --green-mid: #67D7C9;
    --green-pale: #C6EFE9;
    --green-mist: #F3FBFA;
    --paper: #FFFFFF;
    --ink: #2E3A38;
    --backdrop: #E0E0E0;
  }
  * { margin: 0; padding: 0; box-sizing: border-box; }
  html, body { width: 698px; height: 1200px; overflow: hidden; background: var(--backdrop); }
  .canvas { position: relative; width: 698px; height: 1200px; }

  .sheet { position: absolute; background: var(--paper); overflow: hidden; }
  .sheet > svg { position: absolute; inset: 0; width: 100%; height: 100%; display: block; }
  .letterhead { left: 148px; top: 72px; width: 389px; height: 553px; }
  .envelope-front { left: 79px; top: 732px; width: 544px; height: 197px; }
  .envelope-back { left: 79px; top: 969px; width: 544px; height: 122px; }

  .brand { position: absolute; display: flex; align-items: center; }
  .brand-dot { border-radius: 50%; background: var(--green); flex: none; }
  .brand-name {
    font-family: "Domine", Georgia, serif; font-weight: 700;
    color: var(--green-deep); line-height: 1; white-space: nowrap;
  }
  .letterhead .brand { left: 21px; top: 26px; gap: 7px; }
  .letterhead .brand-dot { width: 29px; height: 29px; }
  .letterhead .brand-name { font-size: 17px; }
  .envelope-front .brand { left: 29px; top: 38px; gap: 14px; }
  .envelope-front .brand-dot { width: 52px; height: 52px; }
  .envelope-front .brand-name { font-size: 29px; }

  .sender { position: absolute; color: var(--ink); font-family: "Urbanist", Arial, sans-serif; }
  .sender-name {
    font-family: "Domine", Georgia, serif; font-weight: 700;
    color: var(--green-deep); line-height: 1; white-space: nowrap; letter-spacing: 0.01em;
  }
  .contact { display: flex; align-items: center; white-space: nowrap; }
  .contact svg { flex: none; stroke: var(--green); fill: none; }
  .letterhead .sender { left: 239px; top: 26px; }
  .letterhead .sender-name { font-size: 10px; margin-bottom: 6px; }
  .letterhead .contact { font-size: 6.6px; gap: 3px; height: 10px; }
  .letterhead .contact svg { width: 7px; height: 7px; }
  .envelope-front .sender { left: 335px; top: 34px; }
  .envelope-front .sender-name { font-size: 15px; margin-bottom: 9px; }
  .envelope-front .contact { font-size: 10px; gap: 5px; height: 14.5px; }
  .envelope-front .contact svg { width: 10px; height: 10px; }

  .footer-mark {
    position: absolute; font-family: "Domine", Georgia, serif; font-weight: 700;
    color: var(--green-mid); line-height: 1; white-space: nowrap;
  }
  .letterhead .footer-mark { right: 20px; top: 526px; font-size: 8px; }
  .envelope-back .footer-mark { right: 26px; top: 92px; font-size: 11px; }

  .fill-mist { fill: var(--green-mist); }
  .fill-pale { fill: var(--green-pale); }
  .fill-mid { fill: var(--green-mid); }
</style>
</head>
<body>
<div class="canvas">

  <section class="sheet letterhead">
    <svg viewBox="0 0 816 1160" preserveAspectRatio="none" aria-hidden="true">
      <path class="fill-mist" d="M0,0 H816 V244 C740,190 640,146 520,146 C500,145 460,150 400,162 C280,190 130,225 0,202 Z"/>
      <path class="fill-pale" d="M0,202 C130,225 280,190 400,162 C460,150 500,145 520,146 L520,150 C470,152 420,162 350,182 C240,214 120,240 0,226 Z"/>
      <path class="fill-mid" d="M340,180 C420,158 470,147 520,146 C640,146 740,190 816,244 V297 C740,240 640,165 510,165 C450,165 400,172 340,180 Z"/>
      <path class="fill-mist" d="M0,1090 C80,1130 180,1148 280,1146 C420,1140 600,1072 760,1064 L816,1066 V1160 H0 Z"/>
      <path class="fill-mid" d="M0,1058 C100,1115 200,1135 280,1133 C330,1132 370,1126 400,1122 C360,1132 320,1146 280,1148 C180,1150 80,1130 0,1090 Z"/>
      <path class="fill-pale" d="M270,1148 C420,1130 560,1085 700,1066 C750,1058 790,1052 816,1052 V1072 C790,1070 750,1070 700,1076 C560,1094 420,1135 270,1150 Z"/>
    </svg>
    <div class="brand"><span class="brand-dot"></span><span class="brand-name">PellowNote</span></div>
    <div class="sender">
      <p class="sender-name">DANIEL HARROWAY</p>
      <p class="contact"><svg viewBox="0 0 12 12" stroke-width="1"><rect x="1" y="2.5" width="10" height="7.5" rx="1"/><path d="M1 3.5 L6 7 L11 3.5"/></svg>dharroway@harrowaylaw.com</p>
      <p class="contact"><svg viewBox="0 0 12 12" stroke-width="1"><path d="M6 11 C3 7.5 2.5 6 2.5 4.5 A3.5 3.5 0 0 1 9.5 4.5 C9.5 6 9 7.5 6 11 Z"/><circle cx="6" cy="4.6" r="1.3"/></svg>4810 N Linden Ave Chicago, IL 60625</p>
    </div>
    <p class="footer-mark">PellowNote</p>
  </section>

  <section class="sheet envelope-front">
    <svg viewBox="0 0 1141 414" preserveAspectRatio="none" aria-hidden="true">
      <path class="fill-mist" d="M0,0 H1141 V335 C1040,270 900,205 780,205 C720,205 640,215 560,235 C400,275 200,330 0,280 Z"/>
      <path class="fill-pale" d="M0,280 C200,330 400,275 560,235 C640,215 720,205 780,205 L780,208 C700,210 620,225 520,250 C360,292 180,345 0,322 Z"/>
      <path class="fill-mid" d="M470,255 C600,220 700,205 780,205 C900,205 1040,270 1141,335 V415 C1040,340 900,225 780,225 C680,225 580,240 470,255 Z"/>
    </svg>
    <div class="brand"><span class="brand-dot"></span><span class="brand-name">PellowNote</span></div>
    <div class="sender">
      <p class="sender-name">DANIEL HARROWAY</p>
      <p class="contact"><svg viewBox="0 0 12 12" stroke-width="1"><rect x="1" y="2.5" width="10" height="7.5" rx="1"/><path d="M1 3.5 L6 7 L11 3.5"/></svg>dharroway@harrowaylaw.com</p>
      <p class="contact"><svg viewBox="0 0 12 12" stroke-width="1"><path d="M6 11 C3 7.5 2.5 6 2.5 4.5 A3.5 3.5 0 0 1 9.5 4.5 C9.5 6 9 7.5 6 11 Z"/><circle cx="6" cy="4.6" r="1.3"/></svg>4810 N Linden Ave Chicago, IL 60625</p>
    </div>
  </section>

  <section class="sheet envelope-back">
    <svg viewBox="0 0 1141 255" preserveAspectRatio="none" aria-hidden="true">
      <path class="fill-mist" d="M0,165 C120,210 260,243 420,243 C600,240 820,175 1000,164 C1060,160 1110,158 1141,160 V255 H0 Z"/>
      <path class="fill-mid" d="M0,112 C120,180 260,225 420,225 C470,225 520,220 560,215 C500,232 460,242 420,243 C260,243 120,210 0,165 Z"/>
      <path class="fill-pale" d="M380,245 C600,215 820,160 1000,140 C1060,134 1110,132 1141,132 V160 C1100,158 1050,160 1000,164 C820,180 600,232 380,247 Z"/>
    </svg>
    <p class="footer-mark">PellowNote</p>
  </section>

</div>
</body>
</html>
```